We are a small business - Tree Care Company owned bt a certified Arborist. We would like an advertis

Hurricane season is approaching. We would like our current and potential customers to hire us for their tree work - safety first.

A little bit about us:

We are GWF-certified and insured, you can be confident that you will be able to trust us on your property. We maintain a clean, organized, and safe working environment.

Our tree service services St Petersburg, Clearwater, Belleair, Seminole, and surrounding tampa bay areas cover anything and everything that you may find yourself needing regarding tree care services.

Some of our specialties include tree pruning and trimming, removal, support, planting, emergency tree service, and much, much more.

For hurricane prep, make sure your trees are properly maintained and inspected for structual issues.

Target Market(s)

late 20's to 65. Homeow

Requirements
Must have
• A Call to action. Call us to schedule a FREE estimate.
• 1-866-413-BOUGH

```html
<!DOCTYPE html>
<html lang="en">
<head>
<meta charset="utf-8">
<title>Canopy Crest – Hurricane Season Tree Care</title>
<link href="https://fonts.googleapis.com/css2?family=PT+Sans:wght@400;700&family=Montserrat:wght@700;800&display=swap" rel="stylesheet">
<style>
  :root {
    --leaf: #2c7c34;
    --leaf-deep: #1f6427;
    --leaf-bright: #3f9a3a;
    --cta-bg: #e4eae1;
    --cta-text: #2a8a32;
    --phone: #f3ea1c;
    --ink-grey: #555a57;
    --paper: #ffffff;
  }
  * { margin: 0; padding: 0; box-sizing: border-box; }
  html, body { width: 1200px; height: 840px; overflow: hidden; background: var(--paper); }
  .flyer { position: relative; width: 1200px; height: 840px; overflow: hidden; font-family: "PT Sans", sans-serif; }
  .flyer-shapes { position: absolute; inset: 0; }
  .brand { position: absolute; left: 130px; top: 52px; width: 430px; text-align: center; }
  .brand-name { display: flex; align-items: center; justify-content: center; gap: 12px;
    font-family: "PT Sans", sans-serif; font-weight: 400; font-size: 54px; line-height: 1; color: var(--leaf-bright); }
  .brand-dot { width: 22px; height: 22px; border-radius: 50%; background: var(--leaf-bright); }
  .brand-rule { height: 2px; background: #8d938f; margin: 10px 8px 6px; }
  .brand-tagline { font-size: 17px; letter-spacing: 5.5px; color: var(--ink-grey); }
  .intro { position: absolute; left: 24px; top: 193px; color: var(--paper); font-size: 22px; line-height: 28px; }
  .intro p { margin-bottom: 11px; }
  .intro .p1 { width: 640px; }
  .intro .p2 { width: 612px; text-align: justify; }
  .intro .p3 { width: 586px; text-align: justify; }
  .intro .p4 { width: 570px; }
  .cta { position: absolute; left: 28px; top: 610px; font-family: "Montserrat", sans-serif; font-weight: 700; color: var(--cta-text); }
  .cta-line { font-size: 37px; line-height: 44px; }
  .cta-free { font-size: 58px; font-weight: 800; line-height: 56px; }
  .phone { position: absolute; left: 28px; top: 768px; font-family: "Montserrat", sans-serif; font-weight: 800;
    font-size: 40px; color: var(--phone); letter-spacing: 0.5px; }
</style>
</head>
<body>
<div class="flyer">
  <svg class="flyer-shapes" width="1200" height="840" viewBox="0 0 1200 840">
    <defs>
      <linearGradient id="greenField" x1="0" y1="0" x2="0.4" y2="1">
        <stop offset="0" stop-color="#2f8236"/>
        <stop offset="1" stop-color="#1f6427"/>
      </linearGradient>
      <linearGradient id="skyCanopy" x1="0" y1="0" x2="0" y2="1">
        <stop offset="0" stop-color="#6fa3d8"/>
        <stop offset="0.6" stop-color="#6f8f5a"/>
        <stop offset="1" stop-color="#9bd046"/>
      </linearGradient>
      <linearGradient id="streetScene" x1="0" y1="0" x2="0" y2="1">
        <stop offset="0" stop-color="#4f7a3c"/>
        <stop offset="0.55" stop-color="#7a8f64"/>
        <stop offset="1" stop-color="#5d5f5c"/>
      </linearGradient>
      <linearGradient id="yardScene" x1="0" y1="0" x2="0" y2="1">
        <stop offset="0" stop-color="#6f8a57"/>
        <stop offset="0.5" stop-color="#5c6a3e"/>
        <stop offset="1" stop-color="#4a3f2c"/>
      </linearGradient>
    </defs>
    <rect class="field" width="1200" height="840" fill="url(#greenField)"/>
    <polygon class="logo-panel" points="0,0 735,0 694,177 0,177" fill="var(--paper)"/>
    <polygon class="photo-frame" points="735,0 1200,0 1200,840 542,840" fill="var(--paper)"/>
    <polygon class="photo photo-crew" role="img" aria-label="Photo: arborist in hard hat and bright green company shirt looking up at tall pines" points="745,0 1200,0 1200,270 683,270" fill="url(#skyCanopy)"/>
    <polygon class="photo photo-truck" role="img" aria-label="Photo: white bucket truck parked on a street with safety cones and crew clearing branches" points="681,279 1200,279 1200,558 617,558" fill="url(#streetScene)"/>
    <polygon class="photo photo-lift" role="img" aria-label="Photo: arborist in an aerial lift pruning an oak while ground crew clears cut wood" points="615,567 1200,567 1200,840 552,840" fill="url(#yardScene)"/>
    <polygon class="cta-panel" points="0,591 526,591 494,738 0,738" fill="var(--cta-bg)"/>
  </svg>

  <div class="brand">
    <div class="brand-name"><span>canopy</span><span class="brand-dot"></span><span>crest</span></div>
    <div class="brand-rule"></div>
    <div class="brand-tagline">PROFESSIONAL TREE CARE</div>
  </div>

  <div class="intro">
    <p class="p1">We are GWF-certified and insured, you can be confident that you will be able to trust us on your property. We maintain a clean, organized, and safe working environment.</p>
    <p class="p2">Our tree service services St Petersburg, Clearwater, Belleair, Seminole, and surrounding tampa bay areas cover anything and everything that you may find yourself needing regarding tree care services.</p>
    <p class="p3">Some of our specialties include tree pruning and trimming, removal, support, planting, emergency tree service, and much, much more.</p>
    <p class="p4">For hurricane prep, make sure your trees are properly maintained and inspected for structual issues.</p>
  </div>

  <div class="cta">
    <div class="cta-line">Call us to schedule a</div>
    <div class="cta-line"><span class="cta-free">FREE</span> estimate.</div>
  </div>

  <div class="phone">1-866-413-BOUGH</div>
</div>
</body>
</html>
```